Whitcombe Framing Works - Card Design

I am looking to use the logo designs that you already did for me to develop a business card. I would like the card to have a black background and be double sided. I want white and green logo and text. I have attached an inspiration photo of a look that I like. I would like to use the Vertical Logo attached to take up the full front side of the card. On the back where I have my name and information, I would like to have the horizontal logo or maybe even just the image of the 'A' and trees without the text. I am open, but I am looking for something clean and simple and I want the green to really pop! Additional files can be found under Design #: 40593216

Target Market(s)

Homeowners

Industry/Entity Type

Construction

Contact Information for Business Card

Name: Marcus Pellow, Title: Project Manager, Phone: 402.555.0147, Email: whitcombeframingworks@mailbarn.net, address: 418 Juniper Ln, Alder Creek, OR 95092, Lic# 2046318

Colors
00AB8E
00BBA5
67D7C9
C6EFE9
E9F9F6

Requirements
Nice to have
• I would like to see the logos that I have already got from SketchHarbor, though I am open to new ones

```html
<!DOCTYPE html>
<html lang="en">
<head>
<meta charset="utf-8">
<title>Whitcombe Framing Works – Business Card</title>
<link href="https://fonts.googleapis.com/css2?family=Montserrat:wght@400;500;700&display=swap" rel="stylesheet">
<style>
  :root {
    --stage: #3a3a3a;
    --card-black: #222222;
    --card-white: #ffffff;
    --green: #12b847;
    --ink: #1e1e1e;
    --logo-white: #ffffff;
  }
  html, body {
    margin: 0;
    width: 1200px;
    height: 1200px;
    overflow: hidden;
    background: var(--stage);
    font-family: "Montserrat", sans-serif;
  }
  .sheet {
    position: relative;
    width: 1200px;
    height: 1200px;
  }
  .card {
    position: absolute;
    left: 180px;
    width: 840px;
    height: 480px;
    border-radius: 34px;
    overflow: hidden;
    background: var(--card-black);
    box-shadow: 0 14px 30px rgba(0,0,0,0.45);
  }
  .card--info { top: 60px; }
  .card--front { top: 660px; }

  .info-curve {
    position: absolute;
    inset: 0;
  }
  .contact {
    position: absolute;
    left: 70px;
    top: 160px;
    color: var(--ink);
  }
  .contact__name {
    margin: 0;
    font-size: 34px;
    font-weight: 700;
    color: var(--green);
    letter-spacing: 0.5px;
    line-height: 1.05;
  }
  .contact__title {
    margin: 2px 0 18px;
    font-size: 19px;
    font-weight: 500;
    letter-spacing: 0.5px;
  }
  .contact__licence {
    margin: 0 0 8px;
    font-size: 18px;
  }
  .contact__list {
    list-style: none;
    margin: 0;
    padding: 0;
    font-size: 17px;
  }
  .contact__list li {
    display: flex;
    align-items: center;
    gap: 12px;
    height: 30px;
  }
  .contact__list svg {
    width: 18px;
    height: 18px;
    flex: none;
    fill: var(--green);
  }

  .brand-mini {
    position: absolute;
    left: 700px;
    top: 130px;
    width: 120px;
    text-align: center;
  }
  .brand-mini__dot {
    display: block;
    width: 48px;
    height: 48px;
    margin: 0 auto 14px;
    border-radius: 50%;
    border: 4px solid var(--logo-white);
    box-sizing: border-box;
  }
  .brand-mini__name {
    margin: 0;
    color: var(--logo-white);
    font-size: 16px;
    font-weight: 700;
    line-height: 1.3;
    letter-spacing: 0.5px;
    text-transform: uppercase;
  }

  .brand-hero {
    position: absolute;
    inset: 0;
    display: flex;
    flex-direction: column;
    align-items: center;
    justify-content: center;
  }
  .brand-hero__dot {
    width: 86px;
    height: 86px;
    border-radius: 50%;
    background: var(--green);
    margin-bottom: 28px;
  }
  .brand-hero__name {
    margin: 0;
    color: var(--logo-white);
    font-weight: 700;
    text-transform: uppercase;
    text-align: center;
    letter-spacing: 4px;
    line-height: 1.1;
    font-size: 58px;
  }
</style>
</head>
<body>
<main class="sheet">

  <section class="card card--info" aria-label="Business card, contact side">
    <svg class="info-curve" viewBox="0 0 840 480" width="840" height="480" aria-hidden="true">
      <path d="M0,0 H455 C665,70 740,285 640,480 H0 Z" fill="var(--green)"/>
      <path d="M0,0 H438 C645,72 712,285 616,480 H0 Z" fill="var(--card-white)"/>
      <path d="M0,0 H422 C612,66 688,270 598,480 H0 Z" fill="var(--card-white)"/>
    </svg>

    <div class="contact">
      <h1 class="contact__name">MARCUS PELLOW</h1>
      <p class="contact__title">PROJECT MANAGER</p>
      <p class="contact__licence">Lic# 2046318</p>
      <ul class="contact__list">
        <li>
          <svg viewBox="0 0 24 24"><path d="M6.6 10.8a15.1 15.1 0 0 0 6.6 6.6l2.2-2.2a1 1 0 0 1 1-.25 11.4 11.4 0 0 0 3.6.57 1 1 0 0 1 1 1V20a1 1 0 0 1-1 1A17 17 0 0 1 3 4a1 1 0 0 1 1-1h3.5a1 1 0 0 1 1 1c0 1.25.2 2.45.57 3.57a1 1 0 0 1-.25 1z"/></svg>
          402.555.0147
        </li>
        <li>
          <svg viewBox="0 0 24 24"><path d="M2 5h20v14H2z M2 5l10 8 10-8" fill="none" stroke="var(--green)" stroke-width="2.4"/></svg>
          whitcombeframingworks@mailbarn.net
        </li>
        <li>
          <svg viewBox="0 0 24 24"><path d="M12 2a7 7 0 0 0-7 7c0 5.2 7 13 7 13s7-7.8 7-13a7 7 0 0 0-7-7zm0 9.5A2.5 2.5 0 1 1 12 6.5a2.5 2.5 0 0 1 0 5z"/></svg>
          418 Juniper Ln, Alder Creek, OR 95092
        </li>
      </ul>
    </div>

    <div class="brand-mini">
      <span class="brand-mini__dot"></span>
      <p class="brand-mini__name">Whitcombe<br>Framing<br>Works</p>
    </div>
  </section>

  <section class="card card--front" aria-label="Business card, brand side">
    <div class="brand-hero">
      <span class="brand-hero__dot"></span>
      <p class="brand-hero__name">Whitcombe<br>Framing Works</p>
    </div>
  </section>

</main>
</body>
</html>
```